Bar Tundrel Menu

We are a new bar in Lower East Side in NYC. The name is Bar Tundrel and we need to create a design for our craft cocktails and food menu. Bar Tundrel is an innovative, laid back, yet elegant American cocktail bar with a slight Russian accent. The theme is icy coolness, with silver and gray accents throughout the décor and features cool but not harsh lighting.

```html
<!DOCTYPE html>
<html lang="en">
<head>
<meta charset="utf-8">
<title>Bar Tundrel Menu</title>
<link href="https://fonts.googleapis.com/css2?family=Montserrat:wght@300;400;600;700;800&family=Libre+Baskerville:wght@700&family=Open+Sans:wght@400;600&display=swap" rel="stylesheet">
<style>
:root{
  --stage:#e3e4e6;
  --paper:#ffffff;
  --paper-shade:#eef0f2;
  --ink:#1b1b1d;
  --ink-soft:#4a4b4f;
  --pill:#222326;
  --pill-text:#ffffff;
  --rule:#c9ccd1;
  --food-warm:#d9a24a;
  --food-green:#5f7f3a;
  --drink-red:#d8413c;
  --drink-amber:#e8a93a;
}
*{box-sizing:border-box;margin:0;padding:0}
html,body{width:1200px;height:848px;overflow:hidden;background:var(--stage)}
.stage{position:relative;width:1200px;height:848px}
.sheet{position:absolute;top:54px;width:520px;height:740px;background:linear-gradient(160deg,var(--paper) 0%,var(--paper-shade) 55%,var(--paper) 100%);box-shadow:0 6px 18px rgba(0,0,0,.18);overflow:hidden}
.sheet--cocktails{left:60px}
.sheet--food{left:620px}

/* cocktail sheet */
.cocktail-head{position:absolute;top:34px;left:0;width:372px;height:40px;background:var(--pill);color:var(--pill-text);font:600 20px/40px "Montserrat",sans-serif;letter-spacing:1.5px;padding-left:34px}
.cocktail-price{position:absolute;top:30px;left:334px;width:50px;height:50px;border-radius:50%;background:var(--paper);border:3px solid var(--pill);font:700 19px/44px "Montserrat",sans-serif;text-align:center;color:var(--ink)}
.menu-lettering{position:absolute;top:18px;right:28px;width:100px;height:56px;background:linear-gradient(180deg,#9a9ca0,#55575b);border-radius:4px}
.cocktail-list{position:absolute;top:96px;left:34px;width:380px;list-style:none}
.cocktail{margin-bottom:7px}
.cocktail-name{font:700 15px/1.2 "Libre Baskerville",serif;color:var(--ink)}
.cocktail-spec{font:400 9.5px/1.3 "Open Sans",sans-serif;color:var(--ink-soft)}
.glasses{position:absolute;right:22px;width:84px;height:64px;border-radius:6px;background:linear-gradient(90deg,var(--drink-red),var(--drink-amber) 55%,#cfe4ef)}
.glasses--top{top:92px}
.glasses--mid{top:300px}
.glasses--low{top:470px}

/* food sheet */
.food-header{position:absolute;top:0;left:0;width:520px;height:104px;background:linear-gradient(180deg,#d5d7da,#f4f4f5 60%,#c4c7cb);clip-path:polygon(0 0,100% 0,100% 78%,50% 100%,0 78%)}
.brand{position:absolute;top:26px;left:0;width:520px;text-align:center;font:300 36px/1 "Montserrat",sans-serif;letter-spacing:8px;color:var(--ink)}
.menu-title{position:absolute;top:118px;left:78px;width:230px;text-align:center;font:800 24px/1 "Montserrat",sans-serif;letter-spacing:1px;color:var(--ink)}
.food-list{position:absolute;top:152px;left:34px;width:300px;list-style:none}
.dish{position:relative;height:46px}
.dish-name{display:block;height:24px;background:var(--pill);color:var(--pill-text);font:700 13px/24px "Montserrat",sans-serif;letter-spacing:.6px;padding-left:14px;border-radius:2px 12px 12px 2px;width:268px}
.dish-price{position:absolute;top:-2px;right:0;width:46px;height:28px;border-radius:14px;background:var(--pill);color:var(--pill-text);font:700 14px/28px "Montserrat",sans-serif;text-align:center;border:2px solid var(--paper)}
.dish-notes{display:block;padding:3px 0 0 14px;font:600 9.5px/1.2 "Open Sans",sans-serif;color:var(--ink-soft)}
.food-photo{position:absolute;width:112px;height:112px;border-radius:50%;border:3px solid var(--paper);box-shadow:0 0 0 1px var(--rule)}
.food-photo--1{top:112px;left:370px;background:radial-gradient(circle,var(--food-warm),#b9762c)}
.food-photo--2{top:234px;left:370px;background:radial-gradient(circle,#d9694a,#8e3a27)}
.food-photo--3{top:356px;left:370px;background:radial-gradient(circle,#e3c089,#9c6a38)}
.food-photo--4{top:478px;left:370px;background:radial-gradient(circle,var(--food-green),#2f3f22)}
.food-photo--5{top:604px;left:62px;background:radial-gradient(circle,#f1d9a0,#c29a4c)}
.food-photo--6{top:604px;left:196px;background:radial-gradient(circle,#6b4534,#2d1b14)}
.food-photo--7{top:604px;left:370px;background:radial-gradient(circle,#c65a3c,#6f3a2a)}
</style>
</head>
<body>
<main class="stage">

  <section class="sheet sheet--cocktails" aria-label="Signature cocktails">
    <div class="cocktail-head">SIGNATURE COCKTAILS</div>
    <div class="cocktail-price">$15</div>
    <div class="menu-lettering" role="img" aria-label="Hand lettered word Menu"></div>
    <div class="glasses glasses--top" role="img" aria-label="Illustration of colourful cocktail glasses"></div>
    <div class="glasses glasses--mid" role="img" aria-label="Illustration of colourful cocktail glasses"></div>
    <div class="glasses glasses--low" role="img" aria-label="Illustration of colourful cocktail glasses"></div>
    <ul class="cocktail-list">
      <li class="cocktail"><p class="cocktail-name">Martini Imperial</p><p class="cocktail-spec">(Nordvik Vodka, Birch Tree Juice, Dry Vermouth)</p></li>
      <li class="cocktail"><p class="cocktail-name">Molotov Cocktail</p><p class="cocktail-spec">(Frostmere Vodka, Espresso Syrup, Toasted Caraway Whipped Cream)</p></li>
      <li class="cocktail"><p class="cocktail-name">The Musher</p><p class="cocktail-spec">(Aquavit, Ginger Syrup, Lime Juice, Linden Honey, Cucumber, Basil)</p></li>
      <li class="cocktail"><p class="cocktail-name">Northern Lights</p><p class="cocktail-spec">(Vodka, Verano Rosé, Lemon Juice, Butterfly Pea Tea Syrup)</p></li>
      <li class="cocktail"><p class="cocktail-name">Lost Surfer</p><p class="cocktail-spec">(Aged Rum, Amontillado Sherry, Maple Syrup, Lime Juice, Pineapple)</p></li>
      <li class="cocktail"><p class="cocktail-name">Seward's Folly</p><p class="cocktail-spec">(Rye Whiskey, Dry Vermouth, Pear Compote, Spiced Cherry Bitters)</p></li>
      <li class="cocktail"><p class="cocktail-name">From Folly to Fortune</p><p class="cocktail-spec">(Vermouth, Aperitivo Bianco, Verano Blanc, Orange Bitters)</p></li>
      <li class="cocktail"><p class="cocktail-name">Anchorage 76</p><p class="cocktail-spec">(Dill Infused Vodka, Elderflower Syrup, Lemon Juice, Champagne)</p></li>
      <li class="cocktail"><p class="cocktail-name">Cold, Cold Heart</p><p class="cocktail-spec">(Frostmere Vodka, Beet Syrup, Lemon Juice, Celery Bitters)</p></li>
      <li class="cocktail"><p class="cocktail-name">Back to our Roots</p><p class="cocktail-spec">(Volkova Vodka, Carrot Juice, Ginger Syrup, Lemon Juice)</p></li>
      <li class="cocktail"><p class="cocktail-name">Ancient Spirits</p><p class="cocktail-spec">(Islay Scotch, Honey Liqueur, Lemon Juice, Cardamom Bitters)</p></li>
      <li class="cocktail"><p class="cocktail-name">Denali Sunset</p><p class="cocktail-spec">(Gin, Coconut Syrup, Lemon Juice, Egg White, Rosehip Tea)</p></li>
      <li class="cocktail"><p class="cocktail-name">Forget-Me-Not</p><p class="cocktail-spec">(Fjellgard Gin, Verano Blanc, Lemon Juice, Strawberry Syrup, Egg White)</p></li>
      <li class="cocktail"><p class="cocktail-name">The Torch</p><p class="cocktail-spec">(Harrow Creek Bourbon, Amaro Nero, Chambry Blanc Vermouth, Mango Puree)</p></li>
      <li class="cocktail"><p class="cocktail-name">Spice Trader</p><p class="cocktail-spec">(Cayo Blanco Light Rum, Extra Dry Vermouth, Orange Juice, Spiced Honey)</p></li>
      <li class="cocktail"><p class="cocktail-name">Beyond the Border</p><p class="cocktail-spec">(Mezcal, Pear Puree, Lime Juice, Agave Nectar, Rosemary, Black Walnut Bitters)</p></li>
    </ul>
  </section>

  <section class="sheet sheet--food" aria-label="Food menu">
    <div class="food-header"></div>
    <h1 class="brand">BAR TUNDREL</h1>
    <h2 class="menu-title">MENU</h2>
    <ul class="food-list">
      <li class="dish"><span class="dish-name">ROYAL OSSETRA CAVIAR</span><span class="dish-price">$40</span></li>
      <li class="dish"><span class="dish-name">OYSTER SHOOTER'S</span><span class="dish-price">$15</span><span class="dish-notes">Vodka , Alaskan Mix , Lime</span></li>
      <li class="dish"><span class="dish-name">SALMON TARTARE</span><span class="dish-price">$15</span><span class="dish-notes">Mango , Avocado , Lemon Vinaigrette , Dill</span></li>
      <li class="dish"><span class="dish-name">ROASTED BEET SALAD</span><span class="dish-price">$12</span><span class="dish-notes">Horseradish Cream , Toasted Pecans , Blue Cheese</span></li>
      <li class="dish"><span class="dish-name">ALASKAN KING CRAB TACO</span><span class="dish-price">$18</span><span class="dish-notes">Cabbage Salad , Chili Mayo , Avocado Mousse</span></li>
      <li class="dish"><span class="dish-name">ROAST BEEF CROSTINI</span><span class="dish-price">$12</span><span class="dish-notes">Caramelized Onion , Red Wine Sauce , Dijon Mustard</span></li>
      <li class="dish"><span class="dish-name">LOBSTER MAC &amp; CHEESE</span><span class="dish-price">$18</span><span class="dish-notes">White Cheddar , Truffle , Herb Bread Crumb</span></li>
      <li class="dish"><span class="dish-name">GRILLED CHEESE BITES</span><span class="dish-price">$18</span><span class="dish-notes">Smoked Ham, Gruyere Cheese, Truffle Butter</span></li>
      <li class="dish"><span class="dish-name">CHOCOLATE CAKE</span><span class="dish-price">$10</span><span class="dish-notes">Vanilla Cream &amp; Strawberry Mint</span></li>
    </ul>
    <div class="food-photo food-photo--1" role="img" aria-label="Photo of fried appetizer"></div>
    <div class="food-photo food-photo--2" role="img" aria-label="Photo of salmon tartare"></div>
    <div class="food-photo food-photo--3" role="img" aria-label="Photo of crab taco"></div>
    <div class="food-photo food-photo--4" role="img" aria-label="Photo of beet salad"></div>
    <div class="food-photo food-photo--5" role="img" aria-label="Photo of lobster mac and cheese"></div>
    <div class="food-photo food-photo--6" role="img" aria-label="Photo of chocolate cake"></div>
    <div class="food-photo food-photo--7" role="img" aria-label="Photo of roast beef crostini"></div>
  </section>

</main>
</body>
</html>
```